RW Frameworks Inc Business cards

We need business cards using our existing logo but slightly modified. Right now the logo says RW Framework Masonry. We want to keep the RW part of the design, but replace the Framework Masonry portion with "FRAMEWORKS". Please see the attached file.
Ideally this would be a blank template so we can add Different Names, titles, and phone numbers later.
On the one side we want only the logo and on the other side the detail. I'm attaching an example for you to see.
Please reach out with any other questions. Our address and other details will be given out once we find a design we like.

Target Market(s)

Construction Industry

```html
<!DOCTYPE html>
<html lang="en">
<head>
<meta charset="utf-8">
<title>RW Frameworks Inc — Business Cards</title>
<link rel="stylesheet" href="https://fonts.googleapis.com/css2?family=Oswald:wght@600&family=Roboto+Condensed:wght@400&family=Open+Sans:wght@400&display=swap">
<style>
  :root {
    --brand-blue: #2a75bb;
    --page-bg: #fdfdfd;
    --card-white: #ffffff;
    --ink-white: #ffffff;
  }
  html, body {
    margin: 0;
    padding: 0;
    width: 1200px;
    height: 1200px;
    overflow: hidden;
    background: var(--page-bg);
  }
  .canvas {
    position: relative;
    width: 1200px;
    height: 1200px;
  }
  .card {
    position: absolute;
    left: 300px;
    width: 556px;
    height: 317px;
    box-sizing: border-box;
  }
  .card--front {
    top: 209px;
    background: var(--card-white);
    border: 1px solid var(--brand-blue);
  }
  .card--back {
    top: 542px;
    background: var(--brand-blue);
    color: var(--ink-white);
  }
  .wordmark {
    position: absolute;
    left: 0;
    right: 0;
    top: 128px;
    display: flex;
    align-items: center;
    justify-content: center;
    gap: 12px;
    font-family: "Roboto Condensed", "Arial Narrow", sans-serif;
    font-weight: 400;
    font-size: 40px;
    letter-spacing: 2px;
    color: var(--brand-blue);
    line-height: 1;
  }
  .wordmark__square {
    width: 26px;
    height: 26px;
    background: var(--brand-blue);
  }
  .identity {
    position: absolute;
    right: 47px; /* right edge at x≈509 */
    width: 200px;
    top: 119px;
    text-align: right;
  }
  .identity__name {
    font-family: "Oswald", "Arial Narrow", sans-serif;
    font-weight: 600;
    font-size: 30px;
    line-height: 32px;
    letter-spacing: 0;
  }
  .identity__title {
    font-family: "Open Sans", Arial, sans-serif;
    font-size: 18px;
    line-height: 18px;
    margin-top: -2px;
  }
  .card--back .identity { left: 9px; right: auto; }
  .divider {
    position: absolute;
    left: 226px;
    top: 98px;
    width: 1px;
    height: 91px;
    background: var(--ink-white);
    opacity: 0.8;
  }
  .contacts {
    position: absolute;
    left: 245px;
    top: 97px;
    margin: 0;
    padding: 0;
    list-style: none;
    font-family: "Roboto Condensed", "Arial Narrow", sans-serif;
    font-size: 20px;
  }
  .contacts__item {
    display: flex;
    align-items: center;
    height: 26px;
    margin-bottom: 7px;
  }
  .contacts__item:nth-child(2) { margin-bottom: 8px; }
  .contacts__icon {
    width: 26px;
    height: 26px;
    margin-right: 11px;
    flex: none;
  }
  .address {
    position: absolute;
    left: 122px;
    top: 248px;
    display: flex;
    align-items: center;
    font-family: "Roboto Condensed", "Arial Narrow", sans-serif;
    font-size: 20px;
  }
  .address__icon {
    width: 18px;
    height: 26px;
    margin-right: 17px;
  }
</style>
</head>
<body>
<main class="canvas">

  <section class="card card--front" aria-label="Card front">
    <div class="wordmark">
      <span class="wordmark__square" aria-hidden="true"></span>
      <span class="wordmark__name">RW FRAMEWORKS</span>
    </div>
  </section>

  <section class="card card--back" aria-label="Card back">
    <div class="identity">
      <div class="identity__name">NAME</div>
      <div class="identity__title">Designation</div>
    </div>

    <div class="divider" aria-hidden="true"></div>

    <ul class="contacts">
      <li class="contacts__item">
        <svg class="contacts__icon" viewBox="0 0 26 26" aria-hidden="true">
          <circle cx="13" cy="13" r="13" fill="#fff"/>
          <path d="M8.5 7.5c.6-.6 1.4-.6 1.9 0l1.3 1.6c.4.5.4 1.2-.1 1.6l-.8.7c.7 1.6 2 2.9 3.6 3.6l.7-.8c.4-.5 1.1-.5 1.6-.1l1.6 1.3c.6.5.6 1.3 0 1.9l-.9.9c-.8.8-2.2.9-3.3.3-2.6-1.4-4.8-3.6-6.2-6.2-.6-1.1-.5-2.5.3-3.3z" fill="var(--brand-blue)"/>
        </svg>
        <span>55501 55502</span>
      </li>
      <li class="contacts__item">
        <svg class="contacts__icon" viewBox="0 0 26 26" aria-hidden="true">
          <circle cx="13" cy="13" r="13" fill="#fff"/>
          <rect x="6.5" y="8.5" width="13" height="9" fill="none" stroke="var(--brand-blue)" stroke-width="1.3"/>
          <path d="M6.5 8.5l6.5 5 6.5-5M6.5 17.5l4.6-4.4M19.5 17.5l-4.6-4.4" fill="none" stroke="var(--brand-blue)" stroke-width="1.2"/>
        </svg>
        <span>hello@rwframeworks.com</span>
      </li>
      <li class="contacts__item">
        <svg class="contacts__icon" viewBox="0 0 26 26" aria-hidden="true">
          <circle cx="13" cy="13" r="13" fill="#fff"/>
          <circle cx="13" cy="13" r="7" fill="none" stroke="var(--brand-blue)" stroke-width="1.2"/>
          <ellipse cx="13" cy="13" rx="3" ry="7" fill="none" stroke="var(--brand-blue)" stroke-width="1"/>
          <rect x="5" y="11" width="16" height="4" fill="var(--brand-blue)"/>
        </svg>
        <span>www.rwframeworks.com</span>
      </li>
    </ul>

    <div class="address">
      <svg class="address__icon" viewBox="0 0 18 26" aria-hidden="true">
        <path d="M9 0C4 0 0 4 0 9c0 6 9 17 9 17s9-11 9-17C18 4 14 0 9 0z" fill="#fff"/>
        <circle cx="9" cy="8.5" r="3.5" fill="var(--brand-blue)"/>
      </svg>
      <span>rwframeworks, Construction Industry,US.</span>
    </div>
  </section>

</main>
</body>
</html>
```